Carpentry and Building Business Card

I'm looking for a business card that is minimalistic and that incorporates the theme of my Velmor logo.
On one side I'd like the VELMOR logo with my details on the other side.
Double sided with curved edges

Target Market(s)

Construction / renovation
Adults

Industry/Entity Type

Tradesman

Contact Information for Business Card

Logo on one side, details on the other

Colors

Designer to choose only greyscale colors for use in the design.

Requirements
Must have
• Nilo Petrakis
VELMOR CONSTRUCT
Carpentry & Building Services
0481236574
Velmorconstruct@brixmail.com
Lic No. 718263D
Nice to have
• Fb and insta icons. @velmorconstruct
Should not have
• No hammer or tool icons please.

No address line.

```html
<!DOCTYPE html>
<html lang="en">
<head>
<meta charset="utf-8">
<title>Velmor Construct – Business Card</title>
<link rel="stylesheet" href="https://fonts.googleapis.com/css2?family=Montserrat:wght@400;500;600&display=swap">
<style>
  :root {
    --backdrop: #eeedee;
    --card: #ffffff;
    --card-back: #fbfbfb;
    --accent: #ef9a43;
    --ink: #111111;
    --text: #434343;
    --rule: #555555;
  }
  * { box-sizing: border-box; margin: 0; padding: 0; }
  html, body {
    width: 1146px;
    height: 1200px;
    overflow: hidden;
    background: var(--backdrop);
    font-family: "Montserrat", sans-serif;
  }
  .card {
    position: absolute;
    left: 190px;
    width: 764px;
    height: 440px;
    border-radius: 30px;
    overflow: hidden;
    background: var(--card);
  }
  .card--front { top: 153px; }
  .card--back { top: 636px; background: var(--card-back); }

  .brand {
    position: absolute;
    top: 0;
    left: 0;
    height: 440px;
    display: flex;
    align-items: center;
    justify-content: center;
    color: var(--ink);
    font-weight: 600;
    letter-spacing: 0;
    line-height: 1;
  }
  .card--front .brand { width: 382px; font-size: 46px; padding-bottom: 2px; }
  .card--back .brand { width: 764px; font-size: 68px; }

  .divider {
    position: absolute;
    left: 382px;
    top: 99px;
    width: 1.5px;
    height: 245px;
    background: var(--rule);
  }
  .details {
    position: absolute;
    left: 398px;
    top: 88px;
    color: var(--text);
  }
  .details__name {
    font-size: 30px;
    font-weight: 500;
    color: var(--ink);
    line-height: 1;
    margin-bottom: 18px;
  }
  .details__name .first { color: var(--accent); font-weight: 600; }
  .details__licence {
    font-size: 19.5px;
    color: var(--accent);
    line-height: 27px;
  }
  .details__licence b { font-weight: 600; }
  .details__company {
    font-size: 19px;
    line-height: 26px;
  }
  .details__trade {
    font-size: 20px;
    line-height: 26px;
  }
  .contacts { list-style: none; margin-top: 12px; }
  .contacts li {
    display: flex;
    align-items: center;
    gap: 12px;
    font-size: 20px;
    line-height: 24px;
    letter-spacing: 0.02em;
  }
  .contacts li.phone { font-size: 22px; }
  .contacts li.small { font-size: 17.5px; letter-spacing: 0.01em; }
  .contacts .icon { width: 14px; height: 14px; flex: none; }
  .icon--square { background: var(--accent); border-radius: 2px; width: 12px !important; height: 12px !important; margin: 0 1px; }
  .icon--circle { border: 2px solid var(--accent); border-radius: 50%; width: 12px !important; height: 12px !important; margin: 0 1px; }

  .footer-band {
    position: absolute;
    left: 0;
    bottom: 0;
    width: 764px;
    height: 19px;
  }
</style>
</head>
<body>

<section class="card card--front" aria-label="Business card, details side">
  <p class="brand">Velmor</p>

  <div class="divider"></div>

  <div class="details">
    <p class="details__name"><span class="first">Nilo</span> Petrakis</p>
    <p class="details__licence"><b>Lic No.</b> 718263D</p>
    <p class="details__company">VELMOR CONSTRUCT</p>
    <p class="details__trade">Carpentry &amp; Building Services</p>
    <ul class="contacts">
      <li class="phone">
        <svg class="icon" viewBox="0 0 24 24" aria-hidden="true"><path fill="#ef9a43" d="M6.6 10.8a15 15 0 0 0 6.6 6.6l2.2-2.2a1 1 0 0 1 1-.25 11.4 11.4 0 0 0 3.6.57 1 1 0 0 1 1 1V20a1 1 0 0 1-1 1A17 17 0 0 1 3 4a1 1 0 0 1 1-1h3.5a1 1 0 0 1 1 1c0 1.25.2 2.45.57 3.57a1 1 0 0 1-.25 1z"/></svg>
        0481236574
      </li>
      <li><span class="icon icon--circle"></span>@velmorconstruct</li>
      <li><span class="icon icon--square"></span>/velmorconstruct</li>
      <li class="small">
        <svg class="icon" viewBox="0 0 24 24" aria-hidden="true"><rect x="2" y="5" width="20" height="14" rx="1" fill="#ef9a43"/><path d="M2.5 6l9.5 7 9.5-7" fill="none" stroke="#fff" stroke-width="1.6"/></svg>
        Velmorconstruct@brixmail.com
      </li>
      <li class="small">
        <svg class="icon" viewBox="0 0 24 24" aria-hidden="true"><circle cx="12" cy="12" r="10" fill="#ef9a43"/><path d="M2 12h20M12 2c3 3 3 17 0 20M12 2c-3 3-3 17 0 20" fill="none" stroke="#fff" stroke-width="1.4"/></svg>
        www.Velmorconstruct.com
      </li>
    </ul>
  </div>

  <svg class="footer-band" viewBox="0 0 764 19" preserveAspectRatio="none" aria-hidden="true">
    <polygon points="0,0 392,0 370,19 0,19" fill="#ef9a43"/>
    <polygon points="402,0 764,0 764,19 380,19" fill="#111111"/>
  </svg>
</section>

<section class="card card--back" aria-label="Business card, brand side">
  <p class="brand">Velmor</p>
</section>

</body>
</html>
```